Criação de Papelaria Profissional para Beleza
A empresa queria:
" Espaço físico tipo loja com cabines exclusivas para depilação, método Espanhol com cera quente. Única com cauterização pós depilação. E espaço dedicado a beleza das mãos e pés "

```html
<!DOCTYPE html>
<html lang="pt-BR">
<head>
<meta charset="UTF-8">
<title>Lumi Depil e Unhas — Crachás</title>
<link rel="stylesheet" href="https://fonts.googleapis.com/css2?family=Montserrat:ital,wght@0,400;0,500;0,600;0,700;1,500&display=swap">
<style>
  :root {
    --page: #ece9e6;
    --plum: #2a1f27;
    --plum-light: #3a2c36;
    --pink: #d6427a;
    --pink-soft: #e96a9a;
    --white: #ffffff;
    --card-light: #f4f4f5;
    --card-shade: #e3e3e6;
    --ink: #2b2b2b;
    --field-line: #5a5a5a;
    --photo: #c9c9c9;
    --photo-dark: #8f8f8f;
  }
  * { box-sizing: border-box; margin: 0; padding: 0; }
  html, body { width: 1200px; height: 1200px; overflow: hidden; }
  body {
    background: var(--page);
    font-family: "Montserrat", sans-serif;
    position: relative;
  }
  .badge {
    position: absolute;
    top: 440px;
    width: 398px;
    height: 628px;
    border-radius: 18px;
    overflow: hidden;
    box-shadow: 0 10px 28px rgba(0,0,0,0.18);
  }
  .badge--front { left: 197px; background: linear-gradient(180deg, var(--plum-light), var(--plum)); }
  .badge--back { left: 643px; background: linear-gradient(160deg, var(--white), var(--card-light) 55%, var(--card-shade)); }
  .badge__slot {
    position: absolute; top: 26px; left: 164px;
    width: 70px; height: 16px; border-radius: 8px;
    background: var(--page);
  }
  .badge__band {
    position: absolute; left: 0; right: 0; bottom: 0; height: 18px;
    background: linear-gradient(90deg, var(--pink), var(--pink-soft));
  }
  .brand {
    position: absolute; top: 120px; left: 0; right: 0;
    display: flex; justify-content: center; align-items: center; gap: 10px;
    font-weight: 600; font-size: 24px; color: var(--pink);
    letter-spacing: 0.5px;
  }
  .brand__dot { width: 14px; height: 14px; border-radius: 50%; background: var(--pink); }
  .photo {
    position: absolute; left: 98px; top: 211px;
    width: 202px; height: 266px; border-radius: 6px;
    background: linear-gradient(180deg, var(--photo), var(--photo-dark));
  }
  .holder__name {
    position: absolute; top: 506px; left: 0; right: 0; text-align: center;
    color: var(--pink); font-weight: 600; font-size: 22px; letter-spacing: 0.5px;
  }
  .holder__role {
    position: absolute; top: 538px; left: 0; right: 0; text-align: center;
    color: var(--white); font-weight: 500; font-style: italic; font-size: 19px;
  }
  .field { position: absolute; left: 26px; width: 346px; }
  .field__label { font-size: 14px; font-weight: 500; color: var(--ink); margin-bottom: 6px; }
  .field__box {
    height: 50px; border: 1.5px solid var(--field-line); border-radius: 8px;
    background: rgba(255,255,255,0.6);
  }
  .field--name { top: 196px; }
  .field--id { top: 294px; }
  .field--dept { top: 392px; }
  .contacts {
    position: absolute; left: 26px; top: 482px; list-style: none;
    display: flex; flex-direction: column; gap: 7px;
  }
  .contacts__item {
    display: flex; align-items: center; gap: 8px;
    font-size: 11px; color: var(--ink); line-height: 1.2;
  }
  .contacts__icon {
    flex: none; width: 16px; height: 16px; border-radius: 50%;
    background: var(--pink); display: flex; align-items: center; justify-content: center;
  }
</style>
</head>
<body>
  <section class="badge badge--front">
    <div class="badge__slot"></div>
    <div class="brand"><span class="brand__dot"></span>Lumi Depil e Unhas</div>
    <div class="photo" role="img" aria-label="Espaço para foto do colaborador"></div>
    <p class="holder__name">NOME E SOBRENOME</p>
    <p class="holder__role">Cargo/Função</p>
    <div class="badge__band"></div>
  </section>

  <section class="badge badge--back">
    <div class="badge__slot"></div>
    <div class="brand"><span class="brand__dot"></span>Lumi Depil e Unhas</div>
    <div class="field field--name"><p class="field__label">Nome:</p><div class="field__box"></div></div>
    <div class="field field--id"><p class="field__label">RG:</p><div class="field__box"></div></div>
    <div class="field field--dept"><p class="field__label">DEPARTAMENTO:</p><div class="field__box"></div></div>
    <ul class="contacts">
      <li class="contacts__item">
        <span class="contacts__icon"><svg width="10" height="10" viewBox="0 0 24 24"><path fill="#fff" d="M6.6 10.8a15 15 0 0 0 6.6 6.6l2.2-2.2c.3-.3.7-.4 1-.2 1.1.4 2.3.6 3.6.6.6 0 1 .4 1 1V20c0 .6-.4 1-1 1A17 17 0 0 1 3 4c0-.6.4-1 1-1h3.5c.6 0 1 .4 1 1 0 1.3.2 2.5.6 3.6.1.3 0 .7-.2 1z"/></svg></span>
        (00) 0000-0000
      </li>
      <li class="contacts__item">
        <span class="contacts__icon"><svg width="10" height="10" viewBox="0 0 24 24"><path fill="#fff" d="M3 5h18v14H3zm2 2v.5l7 4.5 7-4.5V7l-7 4.5z"/></svg></span>
        contato@exemplo.com
      </li>
      <li class="contacts__item">
        <span class="contacts__icon"><svg width="10" height="10" viewBox="0 0 24 24"><circle cx="12" cy="12" r="8" fill="none" stroke="#fff" stroke-width="2.5"/><path d="M4 12h16M12 4c3 3 3 13 0 16M12 4c-3 3-3 13 0 16" fill="none" stroke="#fff" stroke-width="1.8"/></svg></span>
        www.exemplo.com.br
      </li>
      <li class="contacts__item">
        <span class="contacts__icon"><svg width="10" height="10" viewBox="0 0 24 24"><path fill="#fff" d="M12 2a7 7 0 0 0-7 7c0 5 7 13 7 13s7-8 7-13a7 7 0 0 0-7-7zm0 9.5A2.5 2.5 0 1 1 12 6.5a2.5 2.5 0 0 1 0 5z"/></svg></span>
        <span>rua exemplo, nº 00<br>cidade-UF, CEP: 00000-000</span>
      </li>
    </ul>
    <div class="badge__band"></div>
  </section>
</body>
</html>
```